labels on the supplement bottle

put my brand name on the table "Verdanta"
put product name 1
"MORNING CORE MATERNA
–WITH PROBIOTICS–"
put product name 2
"Vitamin D3+ Quercetinol"
put product name 3
"mane focus “
put the advert word that you create for these products
design the green area.
Updates
the product name change to
" Morning Core Materna & Aftercare“
"mane focus" change to "Shine, renewal, Blooming"
underneath the brand add small words "Your daily nature essentials"

```html
<!DOCTYPE html>
<html lang="en">
<head>
<meta charset="utf-8">
<title>Verdanta supplement labels</title>
<link rel="stylesheet" href="https://fonts.googleapis.com/css2?family=Quicksand:wght@500;600;700&display=swap">
<style>
  :root {
    --peach: #fec88f;
    --label-white: #ffffff;
    --brand-red: #be1e2d;
    --accent-orange: #f0922a;
    --icon-orange: #f6b55a;
    --ink: #222222;
    --shadow: rgba(120, 60, 10, 0.18);
  }
  * { box-sizing: border-box; margin: 0; padding: 0; }
  html, body {
    width: 1200px; height: 912px; overflow: hidden;
    background: var(--peach);
    font-family: "Quicksand", sans-serif;
  }
  .canvas { position: relative; width: 1200px; height: 912px; }
  .label {
    position: absolute; top: 270px;
    width: 300px; height: 400px;
    background: var(--label-white);
    border-radius: 6px;
    box-shadow: 0 10px 30px var(--shadow);
    text-align: center;
    color: var(--brand-red);
  }
  .label--prenatal { left: 130px; }
  .label--vitamin { left: 450px; }
  .label--hair { left: 770px; }

  .brand {
    position: absolute; top: 48px; left: 0; right: 0;
    display: flex; align-items: center; justify-content: center; gap: 8px;
  }
  .brand__dot {
    width: 12px; height: 12px; border-radius: 50%;
    background: var(--brand-red);
  }
  .brand__name {
    font-size: 34px; font-weight: 700; letter-spacing: -0.5px;
    color: var(--brand-red);
  }
  .tagline {
    position: absolute; top: 98px; left: 0; right: 0;
    font-size: 7.5px; font-weight: 600; letter-spacing: 0.6px;
    color: var(--brand-red);
  }
  .product-name {
    position: absolute; top: 150px; left: 14px; right: 30px;
    font-size: 17px; font-weight: 700; line-height: 1.05;
    text-transform: uppercase; color: var(--brand-red);
  }
  .label--vitamin .product-name { font-size: 24px; top: 140px; }
  .product-sub {
    display: block; margin-top: 6px;
    font-size: 14px; font-weight: 600; color: var(--ink);
  }
  .icon-slot {
    position: absolute; top: 220px; left: 50%;
    width: 62px; height: 62px; margin-left: -40px;
    border-radius: 50%;
    background: radial-gradient(circle, #fde2bd 0%, var(--icon-orange) 100%);
    opacity: 0.8;
  }
  .count {
    position: absolute; right: 8px; top: 206px;
    writing-mode: vertical-rl; transform: rotate(180deg);
    display: flex; align-items: center; gap: 4px;
    font-size: 10.5px; font-weight: 600; letter-spacing: 0.6px;
    color: var(--accent-orange);
  }
  .count__pill {
    width: 10px; height: 10px; border-radius: 50%;
    background: var(--accent-orange);
  }
  .audience {
    position: absolute; right: 0; top: 206px;
    writing-mode: vertical-rl; transform: rotate(180deg);
    font-size: 6px; font-weight: 600; letter-spacing: 0.3px;
    color: var(--ink); height: 70px; text-align: right;
  }
  .label--hair .count { right: 12px; }
  .purpose {
    position: absolute; top: 302px; left: 20px; right: 34px;
    font-size: 7.5px; font-weight: 500; line-height: 1.2;
    color: var(--ink); text-transform: uppercase;
  }
  .diet {
    position: absolute; top: 330px; left: 20px; right: 34px;
    font-size: 7px; font-weight: 500; color: var(--ink);
  }
  .label--prenatal .diet { font-size: 9px; top: 322px; }
  .band {
    position: absolute; top: 350px; left: 34px; right: 34px;
    height: 15px; background: var(--accent-orange);
    color: #ffffff; font-size: 7px; font-weight: 600;
    letter-spacing: 3.5px; line-height: 15px;
  }
</style>
</head>
<body>
<main class="canvas">

  <section class="label label--prenatal">
    <div class="brand"><span class="brand__dot"></span><span class="brand__name">Verdanta</span></div>
    <p class="tagline">YOUR DAILY NATURE ESSENTIALS</p>
    <h2 class="product-name">Morning Core<br>Materna &amp; Aftercare</h2>
    <div class="icon-slot" role="img" aria-label="Line icon of an expecting mother"></div>
    <p class="count"><span class="count__pill"></span>60 TABLETS</p>
    <p class="diet">VEGETARIAN / GLUTEN FREE</p>
    <p class="band">DIETARY SUPPLEMENT</p>
  </section>

  <section class="label label--vitamin">
    <div class="brand"><span class="brand__dot"></span><span class="brand__name">Verdanta</span></div>
    <p class="tagline">YOUR DAILY NATURE ESSENTIALS</p>
    <h2 class="product-name">Vitamin D3 +<span class="product-sub">QUERCETINOL</span></h2>
    <div class="icon-slot" role="img" aria-label="Line icon of a bone joint"></div>
    <p class="count"><span class="count__pill"></span>60 TABLETS</p>
    <p class="purpose">A dietary supplement to support<br>healthy bone mineral density</p>
    <p class="diet">VEGETARIAN / GLUTEN FREE / SOY FREE</p>
    <p class="band">DIETARY SUPPLEMENT</p>
  </section>

  <section class="label label--hair">
    <div class="brand"><span class="brand__dot"></span><span class="brand__name">Verdanta</span></div>
    <p class="tagline">YOUR DAILY NATURE ESSENTIALS</p>
    <h2 class="product-name">Shine, Renewal,<br>Blooming</h2>
    <div class="icon-slot" role="img" aria-label="Line icon of flowing hair"></div>
    <p class="count"><span class="count__pill"></span>90 TABLETS</p>
    <p class="audience">FOR MEN-WOMEN</p>
    <p class="purpose">A dietary supplement to support<br>hair health and growth</p>
    <p class="diet">VEGETARIAN / GLUTEN FREE</p>
    <p class="band">DIETARY SUPPLEMENT</p>
  </section>

</main>
</body>
</html>
```